Women's health flyer for Vindbro Health & Wellness . for a Women's health conference

I need a flyer , post card 4x 6 or 5 x 7 sized designed , 2 sides focused on my business branding and Women's health. we deliver bespoke care and focus on all phases of women's health and life. I want something aligned with our bespoke whole person care philosophy and that is fresh and forward thinking.
www.vindbro-example.com
This is to help women know they can have care for all phases of life , fertility , postpartum , perimenopause , mental health , wellness, weight loss, increased energy stress , menopause etc
please use knowledge from website about my company , www.vindbro-example.com
I also feel like my brand kit could use an additional secondarily color option in it

Target Market(s)

Women 25-70

Industry/Entity Type

health & Wellness

Colors
0054AA
0677BA
7BADD7
CADEEF
E8F1F8
0094D4
00A9DD
6FCCEA
C7EBF8
E9F6FB
00AB8E
00BBA5
67D7C9
C6EFE9
E9F9F6
59FF00
82FF00
B8FF75
E3FFCB
F4FFEA
E54698
E96AAD
F1A4CE
F9D9EA
FCEFF6
A7469A
B969AE
D3A5CF
EDDBEB
F8F0F9

Requirements
Must have
• photos , my logo, connection to my brand
Nice to have
• something fresh and different
Should not have
• look like a genetic "wellness program"

```html
<!DOCTYPE html>
<html lang="en">
<head>
<meta charset="utf-8">
<title>Vindbro Health &amp; Wellness – Postcard</title>
<link href="https://fonts.googleapis.com/css2?family=Merriweather:wght@700;900&family=Poppins:wght@400;500;600;700&display=swap" rel="stylesheet">
<style>
  :root{
    --navy:#0b5a8e;
    --navy-deep:#07507f;
    --sky:#00a9dd;
    --green:#6bb43f;
    --ink:#1c1c1c;
    --white:#ffffff;
    --page:#e6e8eb;
    --stamp:#cfd1d4;
  }
  *{box-sizing:border-box;margin:0;padding:0}
  html,body{width:1067px;height:1200px;overflow:hidden;background:var(--page)}
  body{position:relative;font-family:'Poppins',sans-serif}
  .postcard{position:absolute;left:153px;width:760px;height:543px;background:var(--white);overflow:hidden;box-shadow:0 2px 10px rgba(0,0,0,.12)}
  .postcard--front{top:37px}
  .postcard--back{top:620px}
  .postcard__art{position:absolute;inset:0;width:760px;height:543px}
  .abs{position:absolute}

  .brand{display:flex;align-items:center;gap:10px;color:var(--navy);font-family:'Merriweather',serif;font-weight:700;line-height:1.15}
  .brand__dot{width:14px;height:14px;border-radius:50%;background:var(--sky);flex:none}
  .front-brand{left:50px;top:70px;font-size:25px;width:270px}
  .front-rule{left:50px;top:166px;width:295px;height:2px;background:var(--green)}
  .headline{left:48px;top:184px;font-family:'Merriweather',serif;font-weight:700;font-size:29px;line-height:1.13;color:var(--navy)}
  .headline__accent{color:var(--green)}
  .intro{left:55px;top:344px;width:650px;text-align:center;font-size:12.5px;line-height:1.32;color:var(--ink)}
  .contact-row{left:0;top:494px;width:760px;display:flex;justify-content:center;align-items:center;gap:12px;color:var(--white);font-weight:600;font-size:16px}
  .contact-row__sep{opacity:.9}
  .contact-item{display:flex;align-items:center;gap:8px}
  .icon{width:17px;height:17px;flex:none}

  .services-pill{left:48px;top:149px;width:270px;height:25px;border-radius:13px;background:var(--sky);color:var(--white);font-weight:700;font-size:19px;line-height:25px;text-align:center}
  .services-sub{left:48px;top:180px;width:270px;text-align:center;color:#dbe9f3;font-size:12px}
  .services{left:48px;top:206px;list-style:none;color:var(--white);font-weight:500;font-size:12px;line-height:1.2}
  .services li{display:flex;align-items:center;gap:14px;height:36px}
  .services .badge{width:30px;height:30px;flex:none}
  .contact-title{left:52px;top:396px;color:var(--white);font-weight:700;font-size:20px}
  .contact-list{left:54px;top:440px;list-style:none;font-weight:600;font-size:15.5px;color:var(--ink)}
  .contact-list li{display:flex;align-items:center;gap:10px;height:27px}
  .back-brand{left:415px;top:80px;width:200px;font-size:22px;text-align:center;justify-content:center}
  .stamp{left:647px;top:26px;width:83px;height:83px;background:var(--stamp)}
</style>
</head>
<body>

<!-- FRONT -->
<section class="postcard postcard--front">
  <svg class="postcard__art" viewBox="0 0 760 543" aria-hidden="true">
    <path d="M300 0 C340 70 355 150 368 215 C382 280 410 315 470 330 L760 300 V0 Z" fill="var(--sky)"/>
    <path d="M318 0 H760 V268 C690 300 610 320 540 330 C460 338 410 300 395 220 C382 150 365 60 318 0 Z" fill="#fff"/>
    <path d="M530 340 C620 330 700 300 760 268 V284 C700 316 620 340 530 346 Z" fill="var(--green)"/>
    <path d="M0 452 C200 428 520 445 760 412 V428 C520 462 220 450 0 478 Z" fill="var(--sky)"/>
    <path d="M0 482 C220 452 520 468 760 434 V543 H0 Z" fill="var(--navy)"/>
  </svg>
  <div class="abs" role="img" aria-label="Photo: woman in a blue blouse and sun hat, arms spread wide facing a bright sea"
       style="left:330px;top:0;width:430px;height:330px;background:linear-gradient(135deg,#eef2f4 0%,#d6e2ec 50%,#9fc0e0 100%);clip-path:path('M0 0 H430 V266 C360 298 290 318 210 328 C130 334 82 300 66 220 C52 150 38 60 0 0 Z')"></div>

  <div class="abs brand front-brand"><span class="brand__dot"></span><span>Vindbro Health &amp; Wellness</span></div>
  <div class="abs front-rule"></div>
  <h1 class="abs headline">We deliver bespoke<br>care and focus on<br><span class="headline__accent">all phases of women's<br>health and life.</span></h1>
  <p class="abs intro">Vindbro combines Traditional Eastern Medicine (T.E.A.M) with modern practices, offering a holistic approach to well-being. This approach considers the interconnectedness of mind, body, and spirit, truly taking the whole person approach to wellbeing</p>

  <div class="abs contact-row">
    <span class="contact-item">
      <svg class="icon" viewBox="0 0 20 20"><circle cx="10" cy="10" r="10" fill="var(--green)"/><path d="M7 5.5l2 2-1 1.3c.7 1.4 1.8 2.5 3.2 3.2l1.3-1 2 2-1.3 1.5c-3.5-.4-6.8-3.7-7.2-7.2z" fill="#fff"/></svg>+1-555-014-2290</span>
    <span class="contact-row__sep">|</span>
    <span class="contact-item">
      <svg class="icon" viewBox="0 0 20 20"><circle cx="10" cy="10" r="10" fill="var(--green)"/><rect x="5" y="6.5" width="10" height="7" rx="1" fill="none" stroke="#fff" stroke-width="1.4"/><path d="M5.3 7l4.7 3.6L14.7 7" fill="none" stroke="#fff" stroke-width="1.4"/></svg>hello@vindbro-example.com</span>
    <span class="contact-row__sep">|</span>
    <span class="contact-item">
      <svg class="icon" viewBox="0 0 20 20"><circle cx="10" cy="10" r="10" fill="var(--green)"/><circle cx="10" cy="10" r="5" fill="none" stroke="#fff" stroke-width="1.3"/><path d="M5 10h10M10 5c-2.5 3-2.5 7 0 10M10 5c2.5 3 2.5 7 0 10" fill="none" stroke="#fff" stroke-width="1.1"/></svg>www.vindbro-example.com</span>
  </div>
</section>

<!-- BACK -->
<section class="postcard postcard--back">
  <svg class="postcard__art" viewBox="0 0 760 543" aria-hidden="true">
    <path d="M0 0 H348 C368 120 372 280 335 392 H0 Z" fill="var(--navy)"/>
    <path d="M0 392 H335 C328 405 322 415 318 422 H0 Z" fill="var(--green)"/>
    <path d="M378 0 C412 150 405 300 358 420 C338 470 352 515 392 543 H412 C372 515 360 470 380 420 C425 300 432 150 398 0 Z" fill="var(--sky)"/>
    <path d="M362 0 C392 150 388 290 342 415 C325 462 330 510 355 543 H365 C342 510 338 462 352 418 C398 290 402 150 372 0 Z" fill="var(--navy-deep)"/>
  </svg>
  <div class="abs" role="img" aria-label="Photo: wooden boardwalk crossing a marsh pond with pine forest and cloud reflections"
       style="left:0;top:0;width:358px;height:130px;background:linear-gradient(160deg,#a9c0d0 0%,#7f9a86 55%,#5f7c5c 100%)"></div>

  <div class="abs services-pill">Our Services</div>
  <p class="abs services-sub">Join us in this revolution of wellbeing</p>
  <ul class="abs services">
    <li><svg class="badge" viewBox="0 0 30 30"><circle cx="15" cy="15" r="13" fill="none" stroke="#fff" stroke-width="1.6"/><circle cx="15" cy="15" r="9" fill="var(--green)"/><path d="M11 15l3 3 5-6" fill="none" stroke="#fff" stroke-width="1.8"/></svg>Customized Corporate Wellness</li>
    <li><svg class="badge" viewBox="0 0 30 30"><circle cx="15" cy="15" r="13" fill="none" stroke="#fff" stroke-width="1.6"/><circle cx="15" cy="15" r="9" fill="var(--green)"/><path d="M11 15l3 3 5-6" fill="none" stroke="#fff" stroke-width="1.8"/></svg><span>Acupunture &amp; Traditional<br>East Asian Medicine</span></li>
    <li><svg class="badge" viewBox="0 0 30 30"><circle cx="15" cy="15" r="13" fill="none" stroke="#fff" stroke-width="1.6"/><circle cx="15" cy="15" r="9" fill="var(--green)"/><path d="M11 15l3 3 5-6" fill="none" stroke="#fff" stroke-width="1.8"/></svg>Retreats</li>
    <li><svg class="badge" viewBox="0 0 30 30"><circle cx="15" cy="15" r="13" fill="none" stroke="#fff" stroke-width="1.6"/><circle cx="15" cy="15" r="9" fill="var(--green)"/><path d="M11 15l3 3 5-6" fill="none" stroke="#fff" stroke-width="1.8"/></svg>Individual Coaching</li>
    <li><svg class="badge" viewBox="0 0 30 30"><circle cx="15" cy="15" r="13" fill="none" stroke="#fff" stroke-width="1.6"/><circle cx="15" cy="15" r="9" fill="var(--green)"/><path d="M11 15l3 3 5-6" fill="none" stroke="#fff" stroke-width="1.8"/></svg>Workshops</li>
  </ul>
  <div class="abs contact-title">Contact</div>
  <ul class="abs contact-list">
    <li><svg class="icon" viewBox="0 0 20 20"><circle cx="10" cy="10" r="10" fill="var(--green)"/><path d="M7 5.5l2 2-1 1.3c.7 1.4 1.8 2.5 3.2 3.2l1.3-1 2 2-1.3 1.5c-3.5-.4-6.8-3.7-7.2-7.2z" fill="#fff"/></svg>+1-555-014-2290</li>
    <li><svg class="icon" viewBox="0 0 20 20"><circle cx="10" cy="10" r="10" fill="var(--green)"/><rect x="5" y="6.5" width="10" height="7" rx="1" fill="none" stroke="#fff" stroke-width="1.4"/><path d="M5.3 7l4.7 3.6L14.7 7" fill="none" stroke="#fff" stroke-width="1.4"/></svg>hello@vindbro-example.com</li>
    <li><svg class="icon" viewBox="0 0 20 20"><circle cx="10" cy="10" r="10" fill="var(--green)"/><circle cx="10" cy="10" r="5" fill="none" stroke="#fff" stroke-width="1.3"/><path d="M5 10h10M10 5c-2.5 3-2.5 7 0 10M10 5c2.5 3 2.5 7 0 10" fill="none" stroke="#fff" stroke-width="1.1"/></svg>www.vindbro-example.com</li>
  </ul>

  <div class="abs brand back-brand"><span class="brand__dot"></span><span>Vindbro Health &amp; Wellness</span></div>
  <div class="abs stamp"></div>
</section>

</body>
</html>
```